Plateau UI App Design

We need to have a proper design for a web app that we currently mocked in Powerpoint (will be provided). This PPT contains about 15 slides. The final app will have about 5-6 screens but with context sensitive elements. we would prefer a workflow based UI, i.e. screens should not be clogged but the interface should behave like a wizard or an QX Plateau UI app.

- Design should be flat and should be Plateau UI / Quilt Style (using this as a design language and tiles / colors)
- The final result has to be much more designed, modern and homogeneous than now.
- We would also need a clickable HTML(5) prototype of the design, please let us know how this can be achieved
- Internet connection does not matter for the project, so has to work just within a browser but does not need to connect to a server (could even be local files)
- This does not need to be a fully functional HTML 5 page, after all it is a prototype / screen design, so it would be more like mouse over / clicking / moving to next screen
- If you cannot deliver HTML5 then please suggest providing something that we can edit easily ourselves (e.g. a Powerpoint again)
- TROVE is the name of our product

Target Market(s)

Financial institutions

Industry/Entity Type

Internet

Requirements
Must have
• Plateau UI / Quilt design

```html
<!DOCTYPE html>
<html lang="en">
<head>
<meta charset="utf-8">
<title>TROVE – Plateau UI web app screens</title>
<link rel="stylesheet" href="https://fonts.googleapis.com/css2?family=Open+Sans:wght@300;400;600;700&display=swap">
<style>
  :root{
    --page:#f4f6f8;
    --band-top:#6fb3ea;
    --band-bottom:#2f8fdc;
    --ink:#2e2e2e;
    --app-bg:#262626;
    --app-bar:#1b1b1b;
    --app-line:#3a3a3a;
    --tab:#3b3b3b;
    --tab-active:#5a5a5a;
    --tile:#f39a1e;
    --tile-dark:#d97f0b;
    --sheet:#ececec;
    --sheet-row:#ffffff;
    --sheet-line:#cfcfcf;
    --muted:#9a9a9a;
    --chart-line:#d9534f;
    --chart-fill:rgba(217,83,79,.18);
    --up:#6cc04a;
    --card:#ffffff;
  }
  *{box-sizing:border-box;margin:0;padding:0}
  html,body{width:1200px;height:3647px;overflow:hidden}
  body{font-family:"Open Sans",Arial,sans-serif;color:var(--ink);background:var(--page)}
  .board{position:relative;width:1200px;height:3647px;overflow:hidden;
    background:linear-gradient(180deg,var(--page) 0,var(--page) 2250px,var(--band-top) 2900px,var(--band-bottom) 3647px)}
  .board-corner{position:absolute;left:0;top:0;width:600px;height:360px;
    background:linear-gradient(135deg,#3e98e0 0,rgba(62,152,224,0) 60%)}
  .board-title{position:absolute;left:0;width:1200px;top:18px;text-align:center;
    font-weight:300;font-size:32px;color:#fff;letter-spacing:.5px}
  .caption{position:absolute;left:44px;font-size:34px;font-weight:400;color:var(--ink);line-height:1.45}

  /* ---------- app screen ---------- */
  .app{position:absolute;width:680px;height:425px;background:var(--app-bg);
    box-shadow:0 14px 40px rgba(0,0,0,.28);overflow:hidden;font-size:9px;color:#ddd}
  .app.large{transform:scale(1.1176);transform-origin:0 0}
  .app-bar{position:absolute;left:0;top:0;width:680px;height:40px;background:var(--app-bar);
    border-bottom:1px solid var(--app-line)}
  .brand{position:absolute;left:12px;top:9px;font-size:17px;font-weight:700;color:#fff;letter-spacing:1px}
  .brand-dot{display:inline-block;width:8px;height:8px;background:var(--tile);margin-right:6px;vertical-align:middle}
  .bar-info{position:absolute;top:6px;height:28px;padding-left:30px;border-left:1px solid var(--app-line)}
  .bar-info::before{content:"";position:absolute;left:8px;top:4px;width:16px;height:18px;border:1px solid #777;border-radius:2px}
  .bar-info.primary{left:120px;width:250px}
  .bar-info.secondary{left:375px;width:200px}
  .bar-title{display:block;font-weight:600;color:#eee;font-size:8.5px}
  .bar-sub{display:block;color:var(--muted);font-size:7.5px;margin-top:2px}
  .bar-tools{position:absolute;right:10px;top:13px;display:flex;gap:6px}
  .bar-tools span{width:14px;height:14px;border:1px solid #666;border-radius:2px}

  .tile-menu{position:absolute;left:8px;top:50px;width:92px}
  .tile{display:flex;align-items:flex-end;height:48px;margin-bottom:6px;padding:0 6px 6px 22px;
    background:var(--tile);color:#fff;font-weight:600;font-size:8.5px;position:relative}
  .tile::before{content:"";position:absolute;left:6px;top:8px;width:10px;height:10px;border:1.5px solid #fff;border-radius:2px}
  .tile.current{background:var(--tile-dark)}
  .sub-brand{position:absolute;left:12px;bottom:12px;font-size:20px;font-weight:700;color:#fff;letter-spacing:1px}

  .workspace{position:absolute;left:110px;top:50px;width:360px;height:365px}
  .tabs{display:flex;gap:2px;height:22px}
  .tab{flex:1;background:var(--tab);color:#bbb;font-size:8px;line-height:22px;padding-left:22px;position:relative}
  .tab::before{content:"";position:absolute;left:8px;top:7px;width:8px;height:8px;border-radius:50%;background:#777}
  .tab.active{background:var(--tab-active);color:#fff}
  .tab.active::before{background:var(--tile)}
  .sheet{margin-top:4px;background:var(--sheet);color:#333;height:170px;padding:6px;position:relative}
  .sheet-head{font-weight:700;font-size:8.5px;color:#222;margin-bottom:4px}
  .row{display:flex;height:18px;line-height:18px;background:var(--sheet-row);border-bottom:1px solid var(--sheet-line);font-size:8px}
  .row .key{width:90px;padding-left:6px;color:#555}
  .row .val{flex:1;color:#222}
  .sheet.with-badge .row{margin-left:56px}
  .badge{position:absolute;left:8px;top:24px;width:44px;height:44px;background:var(--tile);color:#fff;
    font-weight:700;font-size:18px;text-align:center;line-height:44px}
  .badge.second{top:80px;background:#222;color:var(--tile)}
  .strip{margin-top:6px;height:60px;background:#1f1f1f;border:1px solid var(--app-line)}
  .strip .row{background:transparent;color:#bbb;border-bottom:1px solid var(--app-line)}
  .strip .row .key,.strip .row .val{color:#bbb}

  .history{position:absolute;left:478px;top:50px;width:194px;height:165px;background:#1c1c1c;border:1px solid var(--app-line)}
  .panel-title{height:18px;line-height:18px;text-align:center;font-weight:600;color:#eee;font-size:8.5px;
    background:linear-gradient(#444,#2e2e2e)}
  .quote{padding:4px 8px;font-size:11px;font-weight:700;color:#fff}
  .quote .change{color:var(--up);margin-left:4px}
  .history svg{display:block;margin:0 6px}
  .params{position:absolute;left:478px;top:222px;width:194px;height:193px;background:#e9e9e9;color:#333;border:1px solid var(--app-line)}
  .params dl{padding:6px 8px;font-size:7.5px;line-height:13px}
  .params dt{display:inline;font-weight:700}
  .params dd{display:inline}
  .params dd::after{content:"";display:block}
  .params hr{border:0;border-top:1px solid #ccc;margin:4px 0}

  .modal{position:absolute;left:140px;top:95px;width:300px;height:230px;background:#fff;color:#333;
    border:1px solid #999;box-shadow:0 8px 24px rgba(0,0,0,.5)}
  .modal-head{height:20px;line-height:20px;padding-left:8px;background:#3a3a3a;color:#fff;font-weight:600;font-size:8.5px}
  .modal .row{margin:0 8px}
  .modal-actions{position:absolute;right:8px;bottom:8px;display:flex;gap:6px}
  .btn{padding:0 12px;height:18px;line-height:18px;font-size:8px;background:#ddd;color:#333}
  .btn.primary{background:#222;color:#fff}
  .dim{position:absolute;inset:40px 0 0 0;background:rgba(0,0,0,.35)}

  /* ---------- floating detail cards ---------- */
  .chart-card{position:absolute;left:880px;top:255px;width:300px;height:270px;background:var(--card);
    box-shadow:0 8px 24px rgba(0,0,0,.15);padding:14px 16px}
  .chart-card .quote{color:#333;font-size:20px;padding:0 0 8px}
  .detail-card{position:absolute;left:850px;top:1880px;width:320px;height:520px;background:var(--app-bg);
    box-shadow:0 14px 40px rgba(0,0,0,.3);color:#ddd;font-size:14px;overflow:hidden}
  .detail-card .panel-title{height:34px;line-height:34px;font-size:15px}
  .detail-card .quote{font-size:20px;padding:10px 14px}
  .detail-card .params{position:static;width:auto;height:auto;border:0}
  .detail-card .params dl{font-size:13px;line-height:22px;padding:10px 14px}
</style>
</head>
<body>
<div class="board">
  <div class="board-corner"></div>
  <h1 class="board-title">UI, UX Design for web App</h1>

  <!-- Home screen -->
  <section class="app large" style="left:70px;top:190px">
    <header class="app-bar">
      <div class="brand"><span class="brand-dot"></span>TROVE</div>
      <div class="bar-info primary"><span class="bar-title">BOND DESK | NA REGION | LIVE</span><span class="bar-sub">Session 04 · Price review queue</span></div>
      <div class="bar-info secondary"><span class="bar-title">Price Monitor</span><span class="bar-sub">Updated 09:42</span></div>
      <div class="bar-tools"><span></span><span></span><span></span></div>
    </header>
    <nav class="tile-menu">
      <a class="tile current">Dashboard</a><a class="tile">Requests</a><a class="tile">Profiles</a><a class="tile">Reports</a><a class="tile">Settings</a>
    </nav>
    <div class="sub-brand">ARC</div>
    <main class="workspace">
      <div class="tabs"><span class="tab active">Request</span><span class="tab">Pricing</span><span class="tab">Review</span></div>
      <div class="sheet">
        <div class="sheet-head">Request details</div>
        <div class="row"><span class="key">Request ID</span><span class="val">RQ-20418</span></div>
        <div class="row"><span class="key">Issuer</span><span class="val">Northfield Corp</span></div>
        <div class="row"><span class="key">Currency</span><span class="val">USD</span></div>
        <div class="row"><span class="key">Maturity</span><span class="val">2029-06-15</span></div>
        <div class="row"><span class="key">Coupon</span><span class="val">4.25 %</span></div>
        <div class="row"><span class="key">Status</span><span class="val">Open</span></div>
      </div>
      <div class="strip">
        <div class="row"><span class="key">Source</span><span class="val">Bench feed</span></div>
        <div class="row"><span class="key">Owner</span><span class="val">Desk team</span></div>
      </div>
    </main>
    <aside class="history">
      <div class="panel-title">History</div>
      <div class="quote">187.24<span class="change">+0.87 (0.47%)</span></div>
      <svg width="180" height="110" viewBox="0 0 180 110" aria-label="Daily price line chart">
        <g stroke="#333" stroke-width="1"><line x1="0" y1="20" x2="180" y2="20"/><line x1="0" y1="50" x2="180" y2="50"/><line x1="0" y1="80" x2="180" y2="80"/></g>
        <polygon points="10,70 35,40 60,30 85,45 110,35 135,60 160,40 160,95 10,95" fill="var(--chart-fill)"/>
        <polyline points="10,70 35,40 60,30 85,45 110,35 135,60 160,40" fill="none" stroke="var(--chart-line)" stroke-width="2"/>
        <g fill="#fff"><circle cx="10" cy="70" r="2.5"/><circle cx="35" cy="40" r="2.5"/><circle cx="60" cy="30" r="2.5"/><circle cx="85" cy="45" r="2.5"/><circle cx="110" cy="35" r="2.5"/><circle cx="135" cy="60" r="2.5"/><circle cx="160" cy="40" r="2.5"/></g>
        <g fill="#999" font-size="7" text-anchor="middle"><text x="10" y="106">Sa</text><text x="35" y="106">Su</text><text x="60" y="106">Mo</text><text x="85" y="106">Tu</text><text x="110" y="106">We</text><text x="135" y="106">Th</text><text x="160" y="106">Fr</text></g>
      </svg>
    </aside>
    <aside class="params">
      <div class="panel-title">Parameterization</div>
      <dl>
        <dt>Policy :</dt> <dd>Standard ECO</dd>
        <dt>Subnet :</dt> <dd>US Bonds NA</dd>
        <dt>Pricing Method :</dt> <dd>US Bench</dd>
      </dl>
      <hr>
      <dl>
        <dt>Request Profile :</dt> <dd>Standard E</dd>
        <dt>Selection Profile :</dt> <dd>CLOSE Sq</dd>
        <dt>Traceability :</dt> <dd>Standard</dd>
      </dl>
    </aside>
  </section>

  <div class="chart-card">
    <div class="quote">187.24 <span class="change">+0.87 (0.47%)</span></div>
    <svg width="268" height="200" viewBox="0 0 268 200" aria-label="All day statistic line chart">
      <g stroke="#eee" stroke-width="1"><line x1="0" y1="40" x2="268" y2="40"/><line x1="0" y1="90" x2="268" y2="90"/><line x1="0" y1="140" x2="268" y2="140"/></g>
      <polygon points="14,60 52,105 90,70 128,90 166,55 204,120 242,80 242,175 14,175" fill="var(--chart-fill)"/>
      <polyline points="14,60 52,105 90,70 128,90 166,55 204,120 242,80" fill="none" stroke="var(--chart-line)" stroke-width="2"/>
      <g fill="#fff" stroke="var(--chart-line)" stroke-width="1.5"><circle cx="14" cy="60" r="3"/><circle cx="52" cy="105" r="3"/><circle cx="90" cy="70" r="3"/><circle cx="128" cy="90" r="3"/><circle cx="166" cy="55" r="3"/><circle cx="204" cy="120" r="3"/><circle cx="242" cy="80" r="3"/></g>
      <g fill="#777" font-size="11" text-anchor="middle" font-family="Open Sans, sans-serif"><text x="14" y="194">Sa</text><text x="52" y="194">Su</text><text x="90" y="194">Mo</text><text x="128" y="194">Tu</text><text x="166" y="194">We</text><text x="204" y="194">Th</text><text x="242" y="194">Fr</text></g>
    </svg>
  </div>

  <p class="caption" style="top:785px">Home screen :<br>Here can see all day statistic graph</p>

  <!-- Screen 2 -->
  <section class="app" style="left:420px;top:1060px">
    <header class="app-bar">
      <div class="brand"><span class="brand-dot"></span>TROVE</div>
      <div class="bar-info primary"><span class="bar-title">BOND DESK | NA REGION | LIVE</span><span class="bar-sub">Session 04 · Price review queue</span></div>
      <div class="bar-info secondary"><span class="bar-title">Price Monitor</span><span class="bar-sub">Updated 09:42</span></div>
      <div class="bar-tools"><span></span><span></span><span></span></div>
    </header>
    <nav class="tile-menu">
      <a class="tile">Dashboard</a><a class="tile current">Requests</a><a class="tile">Profiles</a><a class="tile">Reports</a><a class="tile">Settings</a>
    </nav>
    <div class="sub-brand">ARC</div>
    <main class="workspace">
      <div class="tabs"><span class="tab">Request</span><span class="tab active">Pricing</span><span class="tab">Review</span></div>
      <div class="sheet with-badge">
        <div class="sheet-head">Pricing step</div>
        <div class="badge">16</div>
        <div class="badge second">R</div>
        <div class="row"><span class="key">Instrument</span><span class="val">NF 4.25 29</span></div>
        <div class="row"><span class="key">Bid</span><span class="val">98.40</span></div>
        <div class="row"><span class="key">Ask</span><span class="val">98.65</span></div>
        <div class="row"><span class="key">Spread</span><span class="val">0.25</span></div>
        <div class="row"><span class="key">Method</span><span class="val">US Bench</span></div>
        <div class="row"><span class="key">Result</span><span class="val">Pending</span></div>
      </div>
      <div class="strip">
        <div class="row"><span class="key">Source</span><span class="val">Bench feed</span></div>
        <div class="row"><span class="key">Owner</span><span class="val">Desk team</span></div>
      </div>
    </main>
    <aside class="history">
      <div class="panel-title">History</div>
      <div class="quote">187.24<span class="change">+0.87 (0.47%)</span></div>
      <svg width="180" height="110" viewBox="0 0 180 110" aria-label="Daily price line chart">
        <g stroke="#333" stroke-width="1"><line x1="0" y1="20" x2="180" y2="20"/><line x1="0" y1="50" x2="180" y2="50"/><line x1="0" y1="80" x2="180" y2="80"/></g>
        <polygon points="10,70 35,40 60,30 85,45 110,35 135,60 160,40 160,95 10,95" fill="var(--chart-fill)"/>
        <polyline points="10,70 35,40 60,30 85,45 110,35 135,60 160,40" fill="none" stroke="var(--chart-line)" stroke-width="2"/>
        <g fill="#999" font-size="7" text-anchor="middle"><text x="10" y="106">Sa</text><text x="35" y="106">Su</text><text x="60" y="106">Mo</text><text x="85" y="106">Tu</text><text x="110" y="106">We</text><text x="135" y="106">Th</text><text x="160" y="106">Fr</text></g>
      </svg>
    </aside>
    <aside class="params">
      <div class="panel-title">Parameterization</div>
      <dl><dt>Policy :</dt> <dd>Standard ECO</dd><dt>Subnet :</dt> <dd>US Bonds NA</dd><dt>Pricing Method :</dt> <dd>US Bench</dd></dl>
      <hr>
      <dl><dt>Request Profile :</dt> <dd>Standard E</dd><dt>Selection Profile :</dt> <dd>CLOSE Sq</dd><dt>Traceability :</dt> <dd>Standard</dd></dl>
    </aside>
  </section>

  <p class="caption" style="top:1560px">Screen 2</p>

  <!-- Screen 3 -->
  <section class="app" style="left:110px;top:1900px">
    <header class="app-bar">
      <div class="brand"><span class="brand-dot"></span>TROVE</div>
      <div class="bar-info primary"><span class="bar-title">BOND DESK | NA REGION | LIVE</span><span class="bar-sub">Session 04 · Price review queue</span></div>
      <div class="bar-info secondary"><span class="bar-title">Price Monitor</span><span class="bar-sub">Updated 09:42</span></div>
      <div class="bar-tools"><span></span><span></span><span></span></div>
    </header>
    <nav class="tile-menu">
      <a class="tile">Dashboard</a><a class="tile">Requests</a><a class="tile current">Profiles</a><a class="tile">Reports</a><a class="tile">Settings</a>
    </nav>
    <div class="sub-brand">ARC</div>
    <main class="workspace">
      <div class="tabs"><span class="tab">Request</span><span class="tab">Pricing</span><span class="tab active">Review</span></div>
      <div class="sheet with-badge">
        <div class="sheet-head">Review step</div>
        <div class="badge">R</div>
        <div class="row"><span class="key">Reviewer</span><span class="val">Desk lead</span></div>
        <div class="row"><span class="key">Outcome</span><span class="val">Accepted</span></div>
        <div class="row"><span class="key">Final price</span><span class="val">98.52</span></div>
        <div class="row"><span class="key">Comment</span><span class="val">Within range</span></div>
        <div class="row"><span class="key">Closed</span><span class="val">09:58</span></div>
      </div>
      <div class="strip">
        <div class="row"><span class="key">Source</span><span class="val">Bench feed</span></div>
        <div class="row"><span class="key">Owner</span><span class="val">Desk team</span></div>
      </div>
    </main>
    <aside class="history">
      <div class="panel-title">History</div>
      <div class="quote">187.24<span class="change">+0.87 (0.47%)</span></div>
      <svg width="180" height="110" viewBox="0 0 180 110" aria-label="Daily price line chart">
        <g stroke="#333" stroke-width="1"><line x1="0" y1="20" x2="180" y2="20"/><line x1="0" y1="50" x2="180" y2="50"/><line x1="0" y1="80" x2="180" y2="80"/></g>
        <polygon points="10,70 35,40 60,30 85,45 110,35 135,60 160,40 160,95 10,95" fill="var(--chart-fill)"/>
        <polyline points="10,70 35,40 60,30 85,45 110,35 135,60 160,40" fill="none" stroke="var(--chart-line)" stroke-width="2"/>
        <g fill="#999" font-size="7" text-anchor="middle"><text x="10" y="106">Sa</text><text x="35" y="106">Su</text><text x="60" y="106">Mo</text><text x="85" y="106">Tu</text><text x="110" y="106">We</text><text x="135" y="106">Th</text><text x="160" y="106">Fr</text></g>
      </svg>
    </aside>
    <aside class="params">
      <div class="panel-title">Parameterization</div>
      <dl><dt>Policy :</dt> <dd>Standard ECO</dd><dt>Subnet :</dt> <dd>US Bonds NA</dd><dt>Pricing Method :</dt> <dd>US Bench</dd></dl>
      <hr>
      <dl><dt>Request Profile :</dt> <dd>Standard E</dd><dt>Selection Profile :</dt> <dd>CLOSE Sq</dd><dt>Traceability :</dt> <dd>Standard</dd></dl>
    </aside>
  </section>

  <div class="detail-card">
    <div class="panel-title">History</div>
    <div class="quote">187.24 <span class="change">+0.87 (0.47%)</span></div>
    <svg width="320" height="190" viewBox="0 0 320 190" aria-label="Daily price line chart, enlarged">
      <g stroke="#3a3a3a" stroke-width="1"><line x1="0" y1="30" x2="320" y2="30"/><line x1="0" y1="80" x2="320" y2="80"/><line x1="0" y1="130" x2="320" y2="130"/></g>
      <polygon points="20,110 65,60 110,45 155,70 200,55 245,100 290,65 290,160 20,160" fill="var(--chart-fill)"/>
      <polyline points="20,110 65,60 110,45 155,70 200,55 245,100 290,65" fill="none" stroke="var(--chart-line)" stroke-width="2.5"/>
      <g fill="#fff"><circle cx="20" cy="110" r="3.5"/><circle cx="65" cy="60" r="3.5"/><circle cx="110" cy="45" r="3.5"/><circle cx="155" cy="70" r="3.5"/><circle cx="200" cy="55" r="3.5"/><circle cx="245" cy="100" r="3.5"/><circle cx="290" cy="65" r="3.5"/></g>
      <g fill="#999" font-size="12" text-anchor="middle" font-family="Open Sans, sans-serif"><text x="20" y="182">Sa</text><text x="65" y="182">Su</text><text x="110" y="182">Mo</text><text x="155" y="182">Tu</text><text x="200" y="182">We</text><text x="245" y="182">Th</text><text x="290" y="182">Fr</text></g>
    </svg>
    <aside class="params">
      <div class="panel-title">Parameterization</div>
      <dl><dt>Policy :</dt> <dd>Standard ECO</dd><dt>Subnet :</dt> <dd>US Bonds NA</dd><dt>Pricing Method :</dt> <dd>US Bench</dd></dl>
      <hr>
      <dl><dt>Request Profile :</dt> <dd>Standard E</dd><dt>Selection Profile :</dt> <dd>CLOSE Sq</dd><dt>Traceability :</dt> <dd>Standard</dd></dl>
    </aside>
  </div>

  <p class="caption" style="top:2470px">Screen 3</p>

  <!-- Screen 4 -->
  <section class="app" style="left:110px;top:2680px">
    <header class="app-bar">
      <div class="brand"><span class="brand-dot"></span>TROVE</div>
      <div class="bar-info primary"><span class="bar-title">BOND DESK | NA REGION | LIVE</span><span class="bar-sub">Session 04 · Price review queue</span></div>
      <div class="bar-info secondary"><span class="bar-title">Price Monitor</span><span class="bar-sub">Updated 09:42</span></div>
      <div class="bar-tools"><span></span><span></span><span></span></div>
    </header>
    <nav class="tile-menu">
      <a class="tile">Dashboard</a><a class="tile">Requests</a><a class="tile">Profiles</a><a class="tile current">Reports</a><a class="tile">Settings</a>
    </nav>
    <div class="sub-brand">ARC</div>
    <main class="workspace">
      <div class="tabs"><span class="tab active">Request</span><span class="tab">Pricing</span><span class="tab">Review</span></div>
      <div class="sheet">
        <div class="sheet-head">Request details</div>
        <div class="row"><span class="key">Request ID</span><span class="val">RQ-20418</span></div>
        <div class="row"><span class="key">Issuer</span><span class="val">Northfield Corp</span></div>
        <div class="row"><span class="key">Currency</span><span class="val">USD</span></div>
      </div>
    </main>
    <aside class="history">
      <div class="panel-title">History</div>
      <div class="quote">187.24<span class="change">+0.87 (0.47%)</span></div>
    </aside>
    <aside class="params">
      <div class="panel-title">Parameterization</div>
      <dl><dt>Policy :</dt> <dd>Standard ECO</dd><dt>Subnet :</dt> <dd>US Bonds NA</dd><dt>Pricing Method :</dt> <dd>US Bench</dd></dl>
    </aside>
    <div class="dim"></div>
    <div class="modal">
      <div class="modal-head">New request</div>
      <div class="row"><span class="key">Reference</span><span class="val">RQ-20419</span></div>
      <div class="row"><span class="key">Instrument</span><span class="val">NF 4.25 29</span></div>
      <div class="row"><span class="key">Profile</span><span class="val">Standard E</span></div>
      <div class="row"><span class="key">Due</span><span class="val">Today 17:00</span></div>
      <div class="row"><span class="key">Note</span><span class="val">Month end check</span></div>
      <div class="modal-actions"><span class="btn">Cancel</span><span class="btn primary">OK</span></div>
    </div>
  </section>

  <p class="caption" style="top:3150px">Screen 4</p>
</div>
</body>
</html>
```